Business card design needed

I am branching out into the world of private practice in Speech Pathology. My clients will be aged 0-17; the business card will be distributed within my existing teacher and parent networks in schools.

I work with clients to develop their speech, language, literacy, fluency, swallowing and voice. I like to think that parents hand over their money to me because I've offered a fun session with positive outcomes/growth and for an affordable price.

I'm flexible with colours; though think something bright would be ideal. I'm not wanting anything too cutesy or 'little kid'. I'd like for it to stand out in a bulging purse or on a fridge crammed with papers.

Industry/Entity Type

Teacher

Contact Information for Business Card

Wren Hollow Speech Pathology Pty Ltd
Molly Fenwick
Speech Pathologist
Ph: 0419 826 307
Email: mollyfenwick@quillpost.com

Logo Text

Logo styles of interest
Character Logo
Wordmark Logo
Lettermark Logo
Requirements
Must have
• A kind of graphic to represent the core business - that is, providing intervention to children 0-17 with communication needs (e.g., speech, language, literacy, swallowing, voice, fluency)

Should not have
• Pictures of babies or children.
Love hearts.

```html
<!DOCTYPE html>
<html lang="en">
<head>
<meta charset="utf-8">
<title>Wren Hollow Speech Pathology – Business Card</title>
<link rel="stylesheet" href="https://fonts.googleapis.com/css2?family=League+Spartan:wght@500;600;700&family=Mulish:wght@400;500;600&display=swap">
<style>
  :root {
    --card-yellow: #ffc21a;
    --card-yellow-light: #ffd84a;
    --bubble: #ffe68c;
    --ink: #111111;
    --service-ink: #7a4a08;
    --service-rule: rgba(122, 74, 8, 0.35);
  }
  * { margin: 0; padding: 0; box-sizing: border-box; }
  html, body { width: 1200px; height: 741px; overflow: hidden; }
  body { font-family: "Mulish", sans-serif; color: var(--ink); }

  .card {
    position: relative;
    width: 1200px;
    height: 741px;
    overflow: hidden;
    background: linear-gradient(135deg, var(--card-yellow) 0%, var(--card-yellow) 45%, var(--card-yellow-light) 100%);
  }

  .profile-area {
    position: absolute;
    left: 0; top: 0;
    width: 480px; height: 741px;
    background: linear-gradient(90deg, rgba(255,225,110,0.55) 0%, rgba(255,220,100,0.35) 70%, rgba(255,220,100,0) 100%);
  }

  .services {
    position: absolute;
    left: 64px; top: 118px;
    list-style: none;
    width: 340px;
  }
  .service {
    font-family: "Mulish", sans-serif;
    font-weight: 500;
    font-size: 46px;
    line-height: 1;
    color: var(--service-ink);
    padding: 17px 0;
    border-bottom: 2px solid var(--service-rule);
  }
  .service:last-child { border-bottom: none; }

  .speech-bubble { position: absolute; left: 486px; top: 122px; width: 660px; height: 260px; }

  .brand {
    position: absolute;
    left: 566px; top: 158px;
    display: flex; align-items: center; gap: 26px;
  }
  .brand-name {
    font-family: "League Spartan", sans-serif;
    font-weight: 700;
    font-size: 78px;
    line-height: 0.92;
    letter-spacing: -2px;
  }
  .brand-descriptor {
    font-family: "Mulish", sans-serif;
    font-size: 38px;
    line-height: 1.2;
    font-weight: 400;
  }

  .contact { position: absolute; right: 68px; top: 386px; text-align: right; }
  .contact-name {
    font-family: "League Spartan", sans-serif;
    font-weight: 700; font-size: 58px; line-height: 1; letter-spacing: -1.5px;
  }
  .contact-role {
    font-family: "League Spartan", sans-serif;
    font-weight: 600; font-size: 37px; line-height: 1.1; margin-top: 6px; letter-spacing: 0.5px;
  }
  .contact-line { white-space: nowrap; line-height: 1.1; }
  .contact-line--phone { margin-top: 46px; }
  .contact-line--email { margin-top: 10px; }
  .contact-label { font-size: 28px; }
  .contact-phone { font-size: 46px; letter-spacing: 1px; }
  .contact-email { font-size: 34px; }
</style>
</head>
<body>
  <main class="card">
    <div class="profile-area" role="img" aria-label="Soft light silhouette of a speaking head in profile, facing right"></div>

    <ul class="services">
      <li class="service">speech</li>
      <li class="service">language</li>
      <li class="service">literacy</li>
      <li class="service">fluency</li>
      <li class="service">swallowing</li>
      <li class="service">voice</li>
    </ul>

    <svg class="speech-bubble" viewBox="0 0 660 260" aria-hidden="true">
      <path d="M130 4 H550 A108 108 0 0 1 550 220 H130 A108 108 0 0 1 62 196 L6 246 L34 160 A108 108 0 0 1 130 4 Z"
            fill="var(--bubble)"/>
    </svg>

    <div class="brand">
      <div class="brand-name">Wren<br>Hollow</div>
      <div class="brand-descriptor">Speech<br>Pathology<br>Pty Ltd</div>
    </div>

    <section class="contact">
      <h1 class="contact-name">Molly Fenwick</h1>
      <p class="contact-role">Speech Pathologist</p>
      <p class="contact-line contact-line--phone"><span class="contact-label">Phone: </span><span class="contact-phone">0419 826 307</span></p>
      <p class="contact-line contact-line--email"><span class="contact-label">Email: </span><span class="contact-email">mollyfenwick@quillpost.com</span></p>
    </section>
  </main>
</body>
</html>
```